Recruitment technology firm needs a downloadable pdf to generate leads.

We need design work for a downloadable pdf that will serve as an educational document to visitors to our website. We help clients identify candidates that fit their job posting. We do that by defining the personality of the job and then assessing the personality of the candidates. We then mathematically compare and rank all the candidates against the job. Our colour scheme is blue. The final design should move from communicating a lack of fit or frustration to people fitting their job and success per the text we have built. People who download this lead generator will be added to our email list for re-marketing purposes. our website is www.tallowridgeadvisory.com. I've attached an example of a lead generator (ebike)for a business unrelated to ours.

Target Market(s)

Our target market is businesses of 50-300 people, we're targeting business owners or executives of entrepreneurial (vs. corporate) companies.

Colors
85acd3
3377b5
0455a3

Requirements
Must have
• Easy to read so text isn't overwhelming.
Nice to have
• Don't be compelled to use our website photos or those like it. I'd like this to reflect entrepreneurial companies, not corporate, suit and tie companies.

```html
<!DOCTYPE html>
<html lang="en">
<head>
<meta charset="utf-8">
<title>5 Reasons You Suck at Hiring for Fit</title>
<link rel="stylesheet" href="https://fonts.googleapis.com/css2?family=Montserrat:ital,wght@0,500;0,600;0,700;0,800;1,400&family=Open+Sans:ital,wght@0,400;0,600;0,700;1,400&display=swap">
<style>
  :root {
    --blue-light: #85acd3;
    --blue-mid: #3377b5;
    --blue-deep: #0455a3;
    --navy: #0d3f73;
    --ink: #2b2b2b;
    --panel: #e3eef8;
    --white: #ffffff;
  }
  * { margin: 0; padding: 0; box-sizing: border-box; }
  html, body { width: 849px; height: 1200px; overflow: hidden; background: var(--white); }
  .page {
    position: relative; width: 849px; height: 1200px; overflow: hidden;
    font-family: "Open Sans", Arial, sans-serif; color: var(--ink);
  }
  .hero-photo {
    position: absolute; left: 0; top: 0; width: 849px; height: 585px;
    background:
      linear-gradient(180deg, rgba(255,255,255,0.92) 0%, rgba(255,255,255,0.75) 40%, rgba(255,255,255,0) 62%),
      linear-gradient(120deg, #d9d4cd 0%, #b9b0a6 40%, #8f8377 70%, #cfc8c0 100%);
  }
  .hero-band { position: absolute; left: 0; top: 0; width: 849px; height: 585px; }
  .brand {
    position: absolute; top: 34px; right: 44px;
    display: flex; align-items: center; gap: 10px;
    font-family: "Montserrat", sans-serif; font-weight: 700; font-size: 22px;
    color: var(--navy); letter-spacing: 1px;
  }
  .brand-mark { width: 22px; height: 22px; background: var(--blue-mid); }
  .title {
    position: absolute; left: 42px; top: 64px;
    font-family: "Montserrat", sans-serif; font-weight: 800;
    color: var(--navy); line-height: 1.02; text-transform: uppercase;
  }
  .title-line { font-size: 50px; display: block; }
  .title-big { font-size: 96px; letter-spacing: -1px; }
  .title-small { font-size: 50px; }
  .hero-copy { position: absolute; left: 42px; top: 430px; color: var(--white); }
  .hero-head {
    font-family: "Montserrat", sans-serif; font-weight: 700;
    font-size: 32px; line-height: 1.25;
  }
  .hero-sub {
    font-family: "Montserrat", sans-serif; font-weight: 500;
    font-size: 26px; margin-top: 14px;
  }
  .intro {
    position: absolute; left: 42px; top: 604px; width: 765px;
    font-style: italic; font-size: 16px; line-height: 1.45;
  }
  .goal {
    position: absolute; left: 42px; top: 684px;
    font-weight: 700; font-size: 16px; color: var(--blue-deep);
  }
  .reason {
    position: absolute; left: 42px; width: 765px;
    background: var(--panel);
    padding: 0 22px 18px 22px;
  }
  .reason-1 { top: 716px; height: 205px; }
  .reason-2 { top: 932px; height: 212px; }
  .reason-header { display: flex; align-items: center; gap: 16px; margin-left: -22px; }
  .reason-number {
    width: 62px; height: 52px; background: var(--blue-deep); color: var(--white);
    font-family: "Montserrat", sans-serif; font-weight: 800; font-size: 28px;
    display: flex; align-items: center; justify-content: center;
  }
  .reason-title {
    font-family: "Montserrat", sans-serif; font-weight: 700; font-size: 22px; color: var(--navy);
  }
  .reason-body { font-size: 16px; line-height: 1.45; margin-top: 12px; }
  .footer-bar {
    position: absolute; left: 0; bottom: 0; width: 849px; height: 36px;
    background: linear-gradient(90deg, var(--blue-deep), var(--blue-mid));
  }
</style>
</head>
<body>
<div class="page">
  <div class="hero-photo" role="img" aria-label="Photo of a hiring manager at a desk reviewing a candidate's paperwork"></div>
  <svg class="hero-band" viewBox="0 0 849 585" aria-hidden="true">
    <polygon points="0,415 849,352 849,585 0,585" fill="#3377b5" opacity="0.9"/>
  </svg>

  <div class="brand"><span class="brand-mark"></span>TALLOW RIDGE</div>

  <h1 class="title">
    <span class="title-line">5 Reasons</span>
    <span class="title-line">You Suck at</span>
    <span class="title-line"><span class="title-big">Hiring</span> <span class="title-small">for fit.</span></span>
  </h1>

  <div class="hero-copy">
    <p class="hero-head">Hiring the wrong fit is painful,<br>we are with you there.</p>
    <p class="hero-sub">Bad hires ruin your day, every day.</p>
  </div>

  <p class="intro">You want to make sure your next hire is the right one. You know what it's like when you hire the wrong person – they aren't productive, they don't get along with others, there's tension, you have to let them go, and you re-start the whole process over again.</p>

  <p class="goal">Our goal is to help you stop this cycle. Here are 5 mistakes you are likely making.</p>

  <section class="reason reason-1">
    <div class="reason-header">
      <div class="reason-number">1.</div>
      <h2 class="reason-title">You have not defined the obstacles found in the job.</h2>
    </div>
    <p class="reason-body">Every job has its challenges and you need to find someone who will deal with the challenges as a high performer would. Spending too much time in unstructured conversation or putting too much emphasis on selling the role can detract from this key insight. Define the top 2-5 obstacles and learn how the candidate has or would tackle them.</p>
  </section>

  <section class="reason reason-2">
    <div class="reason-header">
      <div class="reason-number">2.</div>
      <h2 class="reason-title">You describe the job using words, not data.</h2>
    </div>
    <p class="reason-body">Detail oriented means different things to different people. You only find out after you have hired someone that they are not detailed enough (or too detailed!). The same can happen when we say a candidate needs to be proactive or risk oriented. You only find out later that you hired too much or too little. You used words and not numbers to define what you needed for the role.</p>
  </section>

  <div class="footer-bar"></div>
</div>
</body>
</html>
```